Web Design Project for Professional/Social Media Networking website

www.SteeringTapestry.com.au

I am launching a professional/social media networking website called SteeringTapestry which raises awareness of Diversity topics that impact professional, education and social communities. The Diversity initiative targets gender, age, disability, sexual orientation, race and ethnicity.

I expect the majority of customers will be professional women aged 18-65 across all industries. This brand is designed to empower, support and promote those people under represented across the specified diversity groups. It will appeal to those looking to improve both their professional & personal lives. This will be a platform or organisations to promote themselves on the website, therefore, this must be a high quality professional looking site.

I am looking for a website that is professional, positive and has impact. This project is for the design and coding of the website. I have an idea what I want to see but also open to creative design on presentation of items, various pages and flow.

The coding will consist of making the design function (not just pretty pictures). We would be looking to have the winner work with us on a going forward basis for website design changes, tweaks or modifications (paid of course). Please be honest with regards to programming/coding experience and skills as the functionality/ease of this website is essential to its success.

Key Objectives
•Build brand awareness and assist in providing synergy with all key marketing strategies.
•Create a fresh and compelling website design reflecting what the business stands for it will also be user-friendly, build the company’s corporate image and appeal to defined target markets.
•Generate search engine compatibility by optimizing the site for all the major search engines.
•Integrate a custom Content Management System (CMS) to ensure all updates can be made with ease, improving operational efficiency and reducing time to market with critical information.
•Social media implantation, to create social awareness and increase repeat visitors to the site

Customers:
*Australian market initially then branching out Internationally

Must Have:
Company logo-Attached

Inspiration
This website will have a bit of a WorkLoop style functionality. http://www.tradewrens.com.au is another good example of the type of functionality I’m looking for. I understand that the functionality will need to be adapted and increased overtime; however, I am looking for the following minimal features:

Option 1l Page craft CMS Design l (Eg: tradewrens.com.au)

Complete Custom Design
User Friendly Navigation Strategy
Information capture forms (Contact Us)
Rotating banner of images on the home page
CMS - Content Management System to make edits and changes
Membership Area
Blog Integration
Calender & Events Integration
Social Media Plugins
Gallery By Category
Custom URL Structures
Multi-level Navigation
Unlimited Pages Via CMS
uMobe & USlate Compatibility

Option 2 l Custom CMS Design

Complete Custom Design
Membership Area
Directory Listing
Calender Integration for Upcoming Events
Search Functionality ( Tagging System : Individual Profile & business )
Basic SEO Integration
Quorra Metrics
Blog Integration
Forum Integration
Search Engine Submission
Social Media Basic Integration, Pinbook, Chirpex etc.
Custom URL Structures
Multi-level Navigation
Unlimited Pages Via CMS

Option 2 would be my preference, however, guidance on the length of time, cost etc would be welcome. I am happy to increase the budget if required as I appreciate there will be more work involved.

I am looking for the home page to be something different with more of a wow factor and something different to the standard page link menu across the top of the screen.

For the home page I am looking for something a little more striking with a visual impact.

Overall
* Not looking for a cookie cutter template
* Home page simplistic and smooth that shows our "brand"
* Modern browser compatible, CSS, Tablet friendly
* FAST Loading, mouseover buttons, custom icons where necessary

Pages Requested in Design (style, fonts, icons, images, etc flow from page to page).
Home Page
Search Results/directory
Members area/profiles of members
About us
Contact Us
News/features
Updates

Industry/Entity Type

Education

Requirements
Must have
• Logo must be at the Top of each webpage

```html
<!DOCTYPE html>
<html lang="en">
<head>
<meta charset="utf-8">
<title>SteeringTapestry – Home</title>
<link rel="stylesheet" href="https://fonts.googleapis.com/css2?family=Source+Sans+3:wght@400;600;700&display=swap">
<style>
:root{
  --page-bg:#e9e9e9;
  --canvas:#ffffff;
  --brand:#1d5fa5;
  --brand-dark:#0c4585;
  --brand-light:#2f78c4;
  --nav-top:#2a73bd;
  --nav-bottom:#0f4f93;
  --nav-active:#0b3f78;
  --text:#666a70;
  --text-dark:#2b2b2b;
  --muted:#9a9a9a;
  --line:#dfe3e8;
  --panel-head:#eef3f8;
  --orange:#e2762a;
  --footer-bg:#f3f2f3;
  --input-border:#cfd4da;
}
*{box-sizing:border-box;margin:0;padding:0}
html,body{width:1200px;height:2228px;overflow:hidden}
body{background:var(--page-bg);font-family:"Source Sans 3",Arial,sans-serif;color:var(--text);position:relative}
.abs{position:absolute}
.sheet{position:absolute;left:15px;top:7px;width:1170px;height:1906px;background:var(--canvas)}
a{color:inherit;text-decoration:none}

/* header */
.utility-links{left:860px;top:21px;width:280px;text-align:right;font-size:12px;color:#8a8a8a;letter-spacing:.3px}
.utility-links span{margin:0 6px;color:#bbb}
.brand{left:52px;top:33px;width:230px;text-align:center}
.brand-square{width:62px;height:62px;background:var(--brand);border-radius:10px;margin:0 auto 10px}
.brand-name{font-size:25px;font-weight:600;color:var(--brand-dark);letter-spacing:.3px;line-height:1}
.search{left:895px;top:101px;width:245px;height:30px;border:1px solid var(--input-border);background:#fff;display:flex}
.search-field{flex:1;font-size:12px;font-style:italic;color:#777;padding:7px 8px}
.search-btn{width:24px;border-left:1px solid var(--input-border);display:flex;align-items:center;justify-content:center}

/* navigation */
.main-nav{left:33px;top:151px;width:1134px;height:57px;display:flex;background:linear-gradient(var(--nav-top),var(--nav-bottom))}
.main-nav a{display:flex;align-items:center;justify-content:center;color:#fff;font-size:16px;font-weight:600;border-right:1px solid rgba(255,255,255,.18)}
.main-nav a:last-child{border-right:0}
.main-nav a.active{background:var(--nav-active)}

/* banner */
.hero{left:33px;top:215px;width:1134px;height:404px;background:linear-gradient(160deg,#c9b9a4 0%,#8a7564 35%,#3a3033 70%,#2a2428 100%)}
.hero-arrow{top:152px;width:34px;height:52px;background:#fff;display:flex;align-items:center;justify-content:center}
.hero-arrow.prev{left:0;border-radius:0 26px 26px 0}
.hero-arrow.next{right:0;border-radius:26px 0 0 26px}
.hero-dots{left:520px;top:384px;display:flex;gap:5px}
.hero-dots i{width:7px;height:7px;border-radius:50%;background:#fff;opacity:.9}
.hero-dots i:first-child{opacity:.55}

/* welcome */
.welcome{left:37px;top:655px;width:800px}
.welcome h1{font-size:21px;font-weight:400;color:var(--brand);letter-spacing:.3px;margin-bottom:6px}
.welcome p{font-size:13.4px;line-height:22px;margin-bottom:12px}

/* panels */
.panel{border:1px solid var(--line);background:#fff}
.panel-head{height:48px;background:var(--panel-head);border-bottom:1px solid var(--line);font-size:19px;color:var(--brand);padding:12px 0 0 21px;letter-spacing:.3px}
.panel-head.blue{background:linear-gradient(var(--brand-light),var(--brand-dark));color:#fff;border-bottom:0}

/* blog */
.blog{left:34px;top:840px;width:799px;height:562px}
.post{width:380px;height:150px}
.post-thumb{left:0;top:0;width:122px;height:95px}
.post-body{left:135px;top:0;width:245px}
.post-title{font-size:13.5px;font-weight:700;color:var(--text-dark);margin-bottom:3px}
.post-text{font-size:13px;line-height:22px}
.post-meta{font-size:13px;color:var(--muted);margin-top:12px}

/* forum */
.forum{left:36px;top:1418px;width:390px;height:475px}
.thread{position:absolute;left:22px;width:346px;border-bottom:1px solid var(--line);padding-bottom:9px}
.thread:last-child{border-bottom:0}
.thread-title{font-size:13.6px;font-weight:600;color:var(--brand)}
.thread-by{font-size:12px;color:var(--brand);margin-top:3px}

/* contact */
.contact{left:440px;top:1418px;width:390px;height:475px}
.contact-intro{left:23px;top:66px;width:340px;font-size:13px;line-height:23px;color:var(--brand)}
.field-label{left:26px;font-size:13px;color:#444}
.field{left:102px;width:248px;height:29px;border:1px solid var(--input-border);background:#fff}
.field.area{height:89px}
.btn{height:30px;border-radius:3px;color:#fff;font-size:14px;font-weight:600;display:flex;align-items:center;justify-content:center;background:linear-gradient(var(--brand-light),var(--brand-dark))}
.btn.soft{background:linear-gradient(#8fb0d6,#5f8bbd)}

/* sidebar */
.members{left:851px;top:636px;width:316px;height:337px}
.member-photo{left:19px;top:66px;width:74px;height:73px;background:linear-gradient(#cfd3d6,#8e9499)}
.member-info{left:105px;top:64px;width:190px;font-size:12.6px;line-height:21.8px}
.member-info strong{color:var(--text-dark);font-weight:600;display:block}
.thumbs{left:10px;top:264px;width:296px;height:54px}
.thumb{top:0;width:54px;height:54px;background:linear-gradient(#d2b8a0,#8c6a58)}

.login{left:851px;top:980px;width:316px;height:193px}
.login-label{left:26px;font-size:13px;font-weight:600;color:var(--text-dark)}
.login-field{left:94px;width:191px;height:28px;border:1px solid var(--input-border)}

.events{left:851px;top:1183px;width:316px;height:327px}
.cal-month{left:0;top:68px;width:316px;text-align:center;font-size:17px;color:var(--brand);letter-spacing:.5px}
.cal-days{left:14px;top:94px;width:288px;height:37px;background:#eeeeee;display:grid;grid-template-columns:repeat(7,1fr);align-items:center;text-align:center;font-size:17px;font-weight:600;color:var(--orange)}
.cal-grid{left:14px;top:138px;width:288px;display:grid;grid-template-columns:repeat(7,1fr);grid-auto-rows:34.3px;text-align:center;font-size:17px;color:var(--brand);align-items:center}

.directory{left:851px;top:1527px;width:316px;height:366px}
.dir-item{left:34px;font-size:13px;color:var(--text)}
.dir-item::before{content:"";position:absolute;left:-13px;top:6px;border-left:5px solid #9aa0a6;border-top:4px solid transparent;border-bottom:4px solid transparent}

/* footer */
.footer{left:0;top:1913px;width:1200px;height:315px;background:var(--footer-bg)}
.footer-brand{left:52px;top:29px;width:230px;text-align:center}
.footer-brand .brand-square{width:58px;height:58px;background:#6e6e6e;border-radius:10px}
.footer-brand .brand-name{color:#555;font-size:24px}
.social{left:56px;top:151px;display:flex;gap:14px;font-size:12px;color:#555}
.social span{display:flex;align-items:center;gap:4px}
.social i{width:14px;height:14px;border-radius:50%;display:inline-block}
.foot-col{top:52px}
.foot-col a{display:block;position:relative;padding-left:16px;font-size:13.4px;color:#555;height:33px}
.foot-col a::before{content:"";position:absolute;left:0;top:5px;border-left:5px solid #888;border-top:4px solid transparent;border-bottom:4px solid transparent}
.footer-rule{left:25px;top:252px;width:1150px;border-top:1px solid #d8d8d8}
.copyright{left:0;top:274px;width:1200px;text-align:center;font-size:11px;color:#888}
</style>
</head>
<body>
<div class="sheet">
  <div class="abs utility-links" style="left:845px">MEMBER LOGIN<span>|</span>BECOME MEMBER<span>|</span>SITEMAP</div>

  <div class="abs brand" style="left:37px;top:26px">
    <div class="brand-square"></div>
    <div class="brand-name">SteeringTapestry</div>
  </div>

  <div class="abs search" style="left:880px;top:94px">
    <div class="search-field">search here..</div>
    <div class="search-btn"><svg width="8" height="10" viewBox="0 0 8 10"><path d="M2 1l4 4-4 4" fill="none" stroke="#666" stroke-width="1.5"/></svg></div>
  </div>

  <nav class="abs main-nav" style="left:18px;top:144px">
    <a style="width:110px">HOME</a>
    <a class="active" style="width:129px">ABOUT US</a>
    <a style="width:179px">UPCOMING EVENT</a>
    <a style="width:142px">CALENDER</a>
    <a style="width:89px">BLOG</a>
    <a style="width:104px">FORUM</a>
    <a style="width:114px">ARTICLE</a>
    <a style="width:122px">SUPPORT</a>
    <a style="width:145px">CONTACT</a>
  </nav>

  <div class="abs hero" style="left:18px;top:208px" role="img" aria-label="Rotating banner photo of a diverse group of smiling professionals">
    <div class="abs hero-arrow prev"><svg width="10" height="14" viewBox="0 0 10 14"><path d="M8 1L2 7l6 6" fill="none" stroke="#1d5fa5" stroke-width="2"/></svg></div>
    <div class="abs hero-arrow next"><svg width="10" height="14" viewBox="0 0 10 14"><path d="M2 1l6 6-6 6" fill="none" stroke="#1d5fa5" stroke-width="2"/></svg></div>
    <div class="abs hero-dots"><i></i><i></i><i></i><i></i></div>
  </div>

  <section class="abs welcome" style="left:22px;top:648px">
    <h1>WELCOME TO OUR WEBSITE MAINPAGE</h1>
    <p>Mauris vel lacus vitae felis vestibulum volutpat. Etiam est nunc, venenatis in, tristique eu, imperdiet ac, nisl. Cum sociis natoque penatibus et magnis dis parturient montes, nascetur ridiculus mus. In iaculis facilisis massa.</p>
    <p>Etiam eu urna. Sed porta. Suspendisse quam leo, molestie sed, luctus quis, feugiat in, pede. Fusce tellus. Sed metus augue, convallis et, vehicula ut, pulvinar eu, ante. Integer orci tellus, tristique vitae, consequat nec, porta vel, lectus. Nulla sit amet diam. Duis non nunc. Nulla rhoncus dictum metus. Curabitur tristique mi condimentum orci.</p>
  </section>

  <section class="abs panel blog" style="left:19px;top:833px">
    <div class="panel-head">RECENT BLOG</div>
    <div class="abs post" style="left:20px;top:73px">
      <div class="abs post-thumb" style="background:linear-gradient(135deg,#e7c3a6,#a0573f)" role="img" aria-label="Photo of joined hands"></div>
      <div class="abs post-body"><div class="post-title">Nunc tempus felis vitae urna.</div><div class="post-text">Vivamus porttitor, neque at volutpat rutrum, purus nisi eleifend libero, a tempus libero lectus feugiat felis. Morbi diam mauris,</div><div class="post-meta">Posted 4 hours ago &nbsp;/&nbsp; Learn More</div></div>
    </div>
    <div class="abs post" style="left:413px;top:73px">
      <div class="abs post-thumb" style="background:linear-gradient(135deg,#d7b08f,#4b3b36)" role="img" aria-label="Photo of a group of friends"></div>
      <div class="abs post-body"><div class="post-title">Nunc tempus felis vitae urna.</div><div class="post-text">Vivamus porttitor, neque at volutpat rutrum, purus nisi eleifend libero, a tempus libero lectus feugiat felis. Morbi diam mauris,</div><div class="post-meta">Posted 4 hours ago &nbsp;/&nbsp; Learn More</div></div>
    </div>
    <div class="abs post" style="left:20px;top:232px">
      <div class="abs post-thumb" style="background:linear-gradient(135deg,#a7b86a,#6a4a2e)" role="img" aria-label="Photo of two children smiling"></div>
      <div class="abs post-body"><div class="post-title">Nunc tempus felis vitae urna.</div><div class="post-text">Vivamus porttitor, neque at volutpat rutrum, purus nisi eleifend libero, a tempus libero lectus feugiat felis. Morbi diam mauris,</div><div class="post-meta">Posted 4 hours ago &nbsp;/&nbsp; Learn More</div></div>
    </div>
    <div class="abs post" style="left:413px;top:232px">
      <div class="abs post-thumb" style="background:radial-gradient(circle,#6bb0a8,#e8e2d4 70%)" role="img" aria-label="Illustration of a tree made of colourful hands"></div>
      <div class="abs post-body"><div class="post-title">Nunc tempus felis vitae urna.</div><div class="post-text">Vivamus porttitor, neque at volutpat rutrum, purus nisi eleifend libero, a tempus libero lectus feugiat felis. Morbi diam mauris,</div><div class="post-meta">Posted 4 hours ago &nbsp;/&nbsp; Learn More</div></div>
    </div>
    <div class="abs post" style="left:20px;top:396px">
      <div class="abs post-thumb" style="background:radial-gradient(circle,#e49a6a,#8fbbe0 55%,#ffffff 75%)" role="img" aria-label="Illustration of a speech bubble made of colourful figures"></div>
      <div class="abs post-body"><div class="post-title">Nunc tempus felis vitae urna.</div><div class="post-text">Vivamus porttitor, neque at volutpat rutrum, purus nisi eleifend libero, a tempus libero lectus feugiat felis. Morbi diam mauris,</div><div class="post-meta">Posted 4 hours ago &nbsp;/&nbsp; Learn More</div></div>
    </div>
    <div class="abs post" style="left:413px;top:396px">
      <div class="abs post-thumb" style="background:linear-gradient(135deg,#9cc28a,#5a4038)" role="img" aria-label="Photo of young friends outdoors"></div>
      <div class="abs post-body"><div class="post-title">Nunc tempus felis vitae urna.</div><div class="post-text">Vivamus porttitor, neque at volutpat rutrum, purus nisi eleifend libero, a tempus libero lectus feugiat felis. Morbi diam mauris,</div><div class="post-meta">Posted 4 hours ago &nbsp;/&nbsp; Learn More</div></div>
    </div>
  </section>

  <section class="abs panel forum" style="left:21px;top:1411px">
    <div class="panel-head">FORUM</div>
    <div class="thread" style="top:64px"><div class="thread-title">Curabitur tristique mi condimentum orci.</div><div class="thread-by">by Rolan Pike on 09 Oct 2012 &nbsp;22:06</div></div>
    <div class="thread" style="top:130px"><div class="thread-title">Ut velit enim, vestibulum non, fermentum nec</div><div class="thread-by">by Rolan Pike on 05 Oct 2012 &nbsp;22:06</div></div>
    <div class="thread" style="top:196px"><div class="thread-title">Nunc tempus felis vitae urna</div><div class="thread-by">by Rolan Pike on 05 Oct 2012 &nbsp;22:06</div></div>
    <div class="thread" style="top:262px"><div class="thread-title">Morbi diam mauris, viverra in, gravida eu, mattis in</div><div class="thread-by">by Rolan Pike on 08 Oct 2012 &nbsp;22:06</div></div>
    <div class="thread" style="top:328px"><div class="thread-title">Pellentesque nibh libero, ultricies eu, sagittis non</div><div class="thread-by">by Rolan Pike on 02 Oct 2012 &nbsp;22:06</div></div>
    <div class="thread" style="top:394px;border-bottom:0"><div class="thread-title">Mauris neque metus malesuada nec</div><div class="thread-by">by Rolan Pike on 01 Oct 2012 &nbsp;22:06</div></div>
  </section>

  <section class="abs panel contact" style="left:425px;top:1411px">
    <div class="panel-head">CONTACT US</div>
    <div class="abs contact-intro">Vamus porttitor, neque at volutpat rutrum, purus nisi eleifend libero, a tempus libero lectus feugiat felis.</div>
    <div class="abs field-label" style="top:133px">Full Name</div><div class="abs field" style="top:128px"></div>
    <div class="abs field-label" style="top:174px">Email add</div><div class="abs field" style="top:169px"></div>
    <div class="abs field-label" style="top:215px">Phone no.</div><div class="abs field" style="top:210px"></div>
    <div class="abs field-label" style="top:256px">City/State</div><div class="abs field" style="top:251px"></div>
    <div class="abs field-label" style="top:300px">Message</div><div class="abs field area" style="top:294px"></div>
    <div class="abs btn" style="left:102px;top:394px;width:80px">Submit</div>
    <div class="abs btn soft" style="left:191px;top:394px;width:82px">Reset</div>
  </section>

  <aside class="abs panel members" style="left:836px;top:629px">
    <div class="panel-head blue">MEET OUR MEMBERS</div>
    <div class="abs member-photo" role="img" aria-label="Member portrait photo"></div>
    <div class="abs member-info"><strong>Member Name</strong>Lorem ipsum dolor sit amet, consectetuer adipiscing elit. Nam cursus. Morbi ut mi. Nullam enim leo, egestas id, condimentum at, laoreet mattis, massa. Sed eleifend nonummy diam. Praesent mauris ante, elementum et.</div>
    <div class="abs thumbs">
      <svg class="abs" style="left:0;top:19px" width="8" height="14" viewBox="0 0 8 14"><path d="M7 0v14L0 7z" fill="#222"/></svg>
      <div class="abs thumb" style="left:18px" role="img" aria-label="Member photo"></div>
      <div class="abs thumb" style="left:86px" role="img" aria-label="Member photo"></div>
      <div class="abs thumb" style="left:154px" role="img" aria-label="Member photo"></div>
      <div class="abs thumb" style="left:222px" role="img" aria-label="Member photo"></div>
      <svg class="abs" style="left:288px;top:19px" width="8" height="14" viewBox="0 0 8 14"><path d="M1 0v14l7-7z" fill="#222"/></svg>
    </div>
  </aside>

  <aside class="abs panel login" style="left:836px;top:973px">
    <div class="panel-head">MEMEBR LOGIN</div>
    <div class="abs login-label" style="top:75px">Username</div><div class="abs login-field" style="top:68px"></div>
    <div class="abs login-label" style="top:111px">Password</div><div class="abs login-field" style="top:104px"></div>
    <div class="abs btn" style="left:95px;top:134px;width:70px">Log In</div>
  </aside>

  <aside class="abs panel events" style="left:836px;top:1176px">
    <div class="panel-head blue">UPCOMING EVENT</div>
    <svg class="abs" style="left:22px;top:74px" width="8" height="12" viewBox="0 0 8 12"><path d="M7 0v12L0 6z" fill="#c9ccd0"/></svg>
    <div class="abs cal-month">AUGUST 2012</div>
    <svg class="abs" style="left:286px;top:74px" width="8" height="12" viewBox="0 0 8 12"><path d="M1 0v12l7-6z" fill="#c9ccd0"/></svg>
    <div class="abs cal-days"><span>S</span><span>M</span><span>T</span><span>W</span><span>T</span><span>F</span><span>S</span></div>
    <div class="abs cal-grid">
      <span></span><span></span><span></span><span></span><span>1</span><span>2</span><span>3</span>
      <span>4</span><span>5</span><span>6</span><span>7</span><span>8</span><span>9</span><span>10</span>
      <span>11</span><span>12</span><span>13</span><span>14</span><span>15</span><span>16</span><span>17</span>
      <span>18</span><span>19</span><span>20</span><span>21</span><span>22</span><span>23</span><span>24</span>
      <span>25</span><span>26</span><span>27</span><span>28</span><span>29</span><span>30</span><span>31</span>
    </div>
  </aside>

  <aside class="abs panel directory" style="left:836px;top:1520px">
    <div class="panel-head">DIRECTORY LIST</div>
    <div class="abs dir-item" style="top:68px">Cras id elit. Integer quis urna.</div>
    <div class="abs dir-item" style="top:101px">Ut ante enim dapibus malesuada</div>
    <div class="abs dir-item" style="top:135px">Fringilla eu condimentum quis,</div>
    <div class="abs dir-item" style="top:168px">Aenean porttitor eros vel dolor.</div>
    <div class="abs dir-item" style="top:201px">Donec convallis pede venenatis nibh.</div>
    <div class="abs dir-item" style="top:235px">Nam eget lacus.</div>
    <div class="abs dir-item" style="top:268px">Aliquam erat volutpat.</div>
    <div class="abs dir-item" style="top:302px">Quisque dignissim congue leo.</div>
  </aside>
</div>

<footer class="abs footer">
  <div class="abs footer-brand">
    <div class="brand-square"></div>
    <div class="brand-name">SteeringTapestry</div>
  </div>
  <div class="abs social">
    <span><i style="background:#3b5b9a"></i>Pinbook</span>
    <span><i style="background:#2fb4e6"></i>Chirpex</span>
    <span><i style="background:#c9302c"></i>Vidstream</span>
    <span><i style="background:#777"></i>WorkLoop</span>
  </div>
  <div class="abs foot-col" style="left:379px"><a>Home</a><a>About Us</a><a>Services</a><a>What We Do</a><a>Clients</a></div>
  <div class="abs foot-col" style="left:524px"><a>Recent Blog</a><a>Testimonials</a><a>Upcoming Events</a><a>Forum</a><a>Partnes</a></div>
  <div class="abs foot-col" style="left:696px"><a>Articles</a><a>Get in Touch</a><a>Directory Lists</a><a>Calender</a><a>Contact form</a></div>
  <div class="abs foot-col" style="left:855px"><a>Support</a><a>Our Members</a><a>FAQ</a><a>Become Member</a><a>Login</a></div>
  <div class="abs foot-col" style="left:1025px"><a>Contact Form</a><a>Sitemap</a><a>Term and Conditions</a><a>Contact Info</a></div>
  <div class="abs footer-rule"></div>
  <div class="abs copyright">© 2012 Company Name. &nbsp;All right reserved. &nbsp;Term of use</div>
</footer>
</body>
</html>
```